Company Profile
Corvane Logistics Sdn Bhd is a well established and experienced freight forwarder in Kuala Lumpur, Malaysia. We specialize in air and sea forwarding, Custom Brokerage and regulatory compliance services, inland transportation,
overseas freighting and warehousing and distribution management. With our dedicated qualified and experienced professionals, we are fully committed to serving our clients.

Our Mission
Based on the motto “Quick, Reliable and Polite”, Corvane Logistics is dedicated to upholding the following three points corporate philosophy:
1. Adhering to the principle that “the customer always comes first”.
2. Contributing to the development of the local community.
3. Making it our duty to be responsible and sincere.

Our Edge
• One-Stop Logistics Solutions
• Extensive Network Throughout Malaysia
• Highly Qualified and Experienced Pool of Professionals
• Comprehensive IT Solutions
• Innovative and Customer-focused Solutions
• Flexible and Consistent in Managing Exceptions
• Total Supply Chain Visibility

Target Market(s)

We sell the logistics services to all the industry in Malaysia. (ONE Stop Logistics Solutions)

Industry/Entity Type

Logistic

Contact Information for Business Card

I want the back of the card to be white with the logo and slogan. i would like to see the logo on the front with the general info.

Requirements
Must have
• Name, Title, Office, Cell, Fax, Email, Address, Website
Nice to have
• Modern Design Business Card

```html
<!DOCTYPE html>
<html lang="en">
<head>
<meta charset="utf-8">
<title>Corvane Logistics – Stationery Set</title>
<link rel="stylesheet" href="https://fonts.googleapis.com/css2?family=Open+Sans:wght@300;400;600;700&family=Raleway:wght@400;500;600&display=swap">
<style>
  :root{
    --ink:#333333;
    --ink-soft:#555555;
    --blue-deep:#2f5ca8;
    --blue-mid:#3b78bd;
    --blue-light:#4c9dcc;
    --paper:#ffffff;
    --page:#ffffff;
  }
  *{box-sizing:border-box;margin:0;padding:0}
  html,body{width:1200px;height:1200px;overflow:hidden;background:var(--page)}
  body{position:relative;font-family:"Open Sans",Arial,sans-serif;color:var(--ink)}

  .sheet{position:absolute;background:var(--paper);overflow:hidden;box-shadow:0 1px 4px rgba(0,0,0,.18)}
  .sheet > svg.art{position:absolute;left:0;top:0;width:100%;height:100%}
  .abs{position:absolute}
  .center{left:0;right:0;text-align:center}

  .slogan{color:#fff;font-weight:600;letter-spacing:.01em}
  .company{color:#fff;font-weight:700}
  .address{color:#fff;font-weight:400}

  .wordmark{display:flex;align-items:center;gap:5px;color:var(--blue-deep);font-weight:600;white-space:nowrap;line-height:1}
  .wordmark .dot{border-radius:50%;background:var(--blue-deep);flex:none}

  .contacts{list-style:none;color:var(--ink);font-weight:400}
  .contacts li{display:flex;align-items:center;gap:3px;white-space:nowrap}
  .contacts .ico{flex:none;background:var(--blue-deep);border-radius:1px;display:inline-flex;align-items:center;justify-content:center}
  .contacts .ico svg{display:block}
  .web b{color:var(--blue-deep);font-weight:600}

  /* folder */
  .folder{left:144px;top:54px;width:436px;height:614px}
  /* letterhead */
  .letter{left:650px;top:72px;width:407px;height:578px}
  .letter .body{left:59px;width:290px;font-size:8px;font-weight:300;line-height:9.8px;color:var(--ink-soft)}
  .letter .body p{text-align:justify;margin-bottom:9px}
  .signature{width:72px;height:26px;background:rgba(51,51,51,.08);border-radius:3px}
  /* cards */
  .card{top:706px;width:247px;height:142px}
  .card-back{left:89px}
  .card-back .heading{top:44px;font-size:7px;color:#fff;font-family:"Raleway",sans-serif;font-weight:500;letter-spacing:.03em}
  .card-back .rule{top:59px;left:104px;width:40px;height:1px;background:rgba(255,255,255,.6)}
  .card-back .services{top:74px;left:18px;right:18px;text-align:center;font-family:"Raleway",sans-serif;font-size:6.3px;line-height:8.2px;color:#fff}
  .person{font-family:"Raleway",sans-serif}
  .person .name{font-size:7.4px;font-weight:600;color:var(--ink);letter-spacing:.02em}
  .person .role{font-size:6px;color:var(--ink-soft)}
  /* envelopes */
  .env-front{left:113px;top:928px;width:456px;height:232px}
  .env-back{left:657px;top:928px;width:456px;height:232px}
</style>
</head>
<body>

<!-- Presentation folder -->
<section class="sheet folder" aria-label="Presentation folder">
  <svg class="art" viewBox="0 0 436 614" preserveAspectRatio="none" aria-hidden="true">
    <defs>
      <linearGradient id="folderBlue" x1="0" y1="0" x2="1" y2="1">
        <stop offset="0" stop-color="#2f5ca8"/><stop offset="1" stop-color="#4c9dcc"/>
      </linearGradient>
    </defs>
    <path d="M0 0H436V26Q218 50 0 26Z" fill="#333"/>
    <path d="M0 188Q218 168 436 188V614H0Z" fill="url(#folderBlue)"/>
  </svg>
  <div class="abs center slogan" style="top:18px;font-size:8.6px">ONE STOP LOGISTICS SOLUTIONS</div>
  <div class="abs center" style="top:140px;display:flex;justify-content:center">
    <div class="wordmark" style="font-size:17px"><span class="dot" style="width:10px;height:10px"></span>Corvane Logistics</div>
  </div>
  <div class="abs center company" style="top:575px;font-size:8.2px">CORVANE LOGISTICS SDN. BHD. (1048326-K)</div>
  <div class="abs center address" style="top:591px;font-size:5px">No. 8B, 2nd Floor, Jalan Seroja Indah 3, Taman Perdana Kota, 41050 Klang, Selangor Darul Ehsan, Malaysia.</div>
</section>

<!-- Letterhead -->
<section class="sheet letter" aria-label="Letterhead">
  <svg class="art" viewBox="0 0 407 578" preserveAspectRatio="none" aria-hidden="true">
    <defs>
      <linearGradient id="letterBlue" x1="0" y1="0" x2="1" y2="0">
        <stop offset="0" stop-color="#2f5ca8"/><stop offset="1" stop-color="#4c9dcc"/>
      </linearGradient>
    </defs>
    <path d="M0 0H407V19Q203 44 0 19Z" fill="#333"/>
    <path d="M0 538Q203 512 407 538V578H0Z" fill="url(#letterBlue)"/>
  </svg>
  <div class="abs center slogan" style="top:11px;font-size:8.6px">ONE STOP LOGISTICS SOLUTIONS</div>
  <div class="abs" style="left:59px;top:100px">
    <div class="wordmark" style="font-size:11px"><span class="dot" style="width:7px;height:7px"></span>Corvane Logistics</div>
  </div>
  <ul class="abs contacts" style="left:266px;top:68px;font-size:5.6px;line-height:9.5px">
    <li><span class="ico" style="width:6px;height:6px"><svg width="4" height="4" viewBox="0 0 10 10"><path d="M2 1l2 2-1 1.5a6 6 0 0 0 2.5 2.5L7 6l2 2-1.5 1.5C4.5 9 1 5.5.5 2.5Z" fill="#fff"/></svg></span>+ (603) 5520 1840 / 1850</li>
    <li><span class="ico" style="width:6px;height:6px"><svg width="4" height="4" viewBox="0 0 10 10"><rect x="1" y="3" width="8" height="6" fill="#fff"/><rect x="3" y="1" width="4" height="3" fill="#fff"/></svg></span>+ (603) 5520 1860</li>
    <li class="web"><span class="ico" style="width:6px;height:6px;border-radius:50%"><svg width="4" height="4" viewBox="0 0 10 10"><circle cx="5" cy="5" r="3.6" fill="none" stroke="#fff" stroke-width="1.2"/></svg></span>www.<b>corvane</b>.com.my</li>
  </ul>
  <div class="abs body" style="top:154px">
    <p>September 1, 2016</p>
    <p>To the Former Stockholders of Tessaline, Inc.:</p>
    <p>Lorem ipsum dolor sit amet, consectetur adipiscing elit, sed do eiusmod tempor incididunt ut labore et dolore magna aliqua. Ut enim ad minim veniam, quis nostrud exercitation ullamco laboris nisi ut aliquip ex ea com modo consequat. Duis aute irure dolor in reprehenderit in voluptate velit esse cillum dolore eu fugiat nulla pariatur. Excepteur sint occaecat cupi datat non proident, sunt in culpa qui officia deserunt mollit anim id est laborum.</p>
    <p>Lorem ipsum dolor sit amet, consectetur adipiscing elit, sed do eiusmod tempor incididunt ut labore et dolore magna aliqua. Ut enim ad minim veniam, quis nostrud exercitation ullamco laboris nisi ut aliquip ex ea com modo consequat. Duis aute irure dolor in reprehenderit in voluptate velit esse cillum dolore eu fugiat nulla pariatur. Excepteur sint occaecat cupi datat non proident, sunt in culpa qui officia deserunt mollit anim id est laborum.</p>
    <p style="margin-top:16px;margin-bottom:4px">Sincerely yours,<br>Halvern Ltd.,</p>
    <p style="margin-bottom:6px">Adrian Lowe<br>CEO</p>
    <div class="signature" role="img" aria-label="Handwritten signature of Adrian Lowe"></div>
  </div>
  <div class="abs center company" style="top:540px;font-size:8.6px">CORVANE LOGISTICS SDN. BHD. (1048326-K)</div>
  <div class="abs center address" style="top:556px;font-size:5.6px">No. 8B, 2nd Floor, Jalan Seroja Indah 3, Taman Perdana Kota, 41050 Klang, Selangor Darul Ehsan, Malaysia.</div>
</section>

<!-- Business card back -->
<section class="sheet card card-back" aria-label="Business card, services side">
  <svg class="art" viewBox="0 0 247 142" preserveAspectRatio="none" aria-hidden="true">
    <defs>
      <linearGradient id="cardBlue" x1="0" y1="0" x2="1" y2="1">
        <stop offset="0" stop-color="#2f5ca8"/><stop offset="1" stop-color="#4c9dcc"/>
      </linearGradient>
    </defs>
    <rect width="247" height="142" fill="url(#cardBlue)"/>
    <path d="M0 0H247V12Q123 27 0 12Z" fill="#333"/>
  </svg>
  <div class="abs center slogan" style="top:7px;font-size:6.2px">ONE STOP LOGISTICS SOLUTIONS</div>
  <div class="abs center heading">WE'RE SPECIALIZE IN</div>
  <div class="abs rule"></div>
  <div class="abs services">• International Shipping (Air / Sea) • Transportation / Haulage<br>• Consolidation – NVOCC • Project Management<br>• Packing • Supply Chain Management • Warehousing<br>• Marine Insurance • Tax Exemption Consultancy • Distribution<br>• Custom Brokerage • Door to Door</div>
</section>

<!-- Business card fronts -->
<section class="sheet card" style="left:354px" aria-label="Business card, contact side">
  <svg class="art" viewBox="0 0 247 142" preserveAspectRatio="none" aria-hidden="true">
    <defs><linearGradient id="cardFront1" x1="0" y1="0" x2="1" y2="0"><stop offset="0" stop-color="#2f5ca8"/><stop offset="1" stop-color="#4c9dcc"/></linearGradient></defs>
    <path d="M0 118Q123 102 247 118V142H0Z" fill="url(#cardFront1)"/>
  </svg>
  <div class="abs" style="left:16px;top:72px"><div class="wordmark" style="font-size:9.6px"><span class="dot" style="width:6px;height:6px"></span>Corvane Logistics</div></div>
  <div class="abs person" style="left:127px;top:18px"><div class="name">NADZRUL HAZIQ</div><div class="role">Managing Director</div></div>
  <ul class="abs contacts" style="left:127px;top:41px;font-size:5.2px;line-height:9px">
    <li><span class="ico" style="width:5px;height:5px"></span>+ 6012-480 2175</li>
    <li style="margin-top:4px"><span class="ico" style="width:5px;height:5px"></span>+ (603) 5520 1840 / 1850</li>
    <li><span class="ico" style="width:5px;height:5px"></span>+ (603) 5520 1860</li>
    <li style="margin-top:6px"><span class="ico" style="width:5px;height:5px"></span>nadzrul.haziq@corvane.com.my</li>
    <li class="web"><span class="ico" style="width:5px;height:5px;border-radius:50%"></span>www.<b>corvane</b>.com.my</li>
  </ul>
  <div class="abs center company" style="top:116px;font-size:5.6px">CORVANE LOGISTICS SDN. BHD. (1048326-K)</div>
  <div class="abs center address" style="top:127px;font-size:3.4px">No. 8B, 2nd Floor, Jalan Seroja Indah 3, Taman Perdana Kota, 41050 Klang, Selangor Darul Ehsan, Malaysia.</div>
</section>

<section class="sheet card" style="left:618px" aria-label="Business card, contact side variant">
  <svg class="art" viewBox="0 0 247 142" preserveAspectRatio="none" aria-hidden="true">
    <defs><linearGradient id="cardFront2" x1="0" y1="0" x2="1" y2="0"><stop offset="0" stop-color="#2f5ca8"/><stop offset="1" stop-color="#4c9dcc"/></linearGradient></defs>
    <path d="M0 118Q123 102 247 118V142H0Z" fill="url(#cardFront2)"/>
  </svg>
  <div class="abs" style="left:28px;top:70px"><div class="wordmark" style="font-size:8.2px"><span class="dot" style="width:5px;height:5px"></span>Corvane Logistics</div></div>
  <div class="abs person" style="left:127px;top:18px"><div class="name">NADZRUL HAZIQ</div><div class="role">Managing Director</div></div>
  <ul class="abs contacts" style="left:127px;top:41px;font-size:5.2px;line-height:9px">
    <li><span class="ico" style="width:5px;height:5px"></span>+ 6012-480 2175</li>
    <li style="margin-top:4px"><span class="ico" style="width:5px;height:5px"></span>+ (603) 5520 1840 / 1850</li>
    <li><span class="ico" style="width:5px;height:5px"></span>+ (603) 5520 1860</li>
    <li style="margin-top:6px"><span class="ico" style="width:5px;height:5px"></span>nadzrul.haziq@corvane.com.my</li>
    <li class="web"><span class="ico" style="width:5px;height:5px;border-radius:50%"></span>www.<b>corvane</b>.com.my</li>
  </ul>
  <div class="abs center company" style="top:116px;font-size:5.6px">CORVANE LOGISTICS SDN. BHD. (1048326-K)</div>
  <div class="abs center address" style="top:127px;font-size:3.4px">No. 8B, 2nd Floor, Jalan Seroja Indah 3, Taman Perdana Kota, 41050 Klang, Selangor Darul Ehsan, Malaysia.</div>
</section>

<section class="sheet card" style="left:882px" aria-label="Business card, contact side compact">
  <svg class="art" viewBox="0 0 247 142" preserveAspectRatio="none" aria-hidden="true">
    <defs><linearGradient id="cardFront3" x1="0" y1="0" x2="1" y2="0"><stop offset="0" stop-color="#2f5ca8"/><stop offset="1" stop-color="#4c9dcc"/></linearGradient></defs>
    <path d="M0 118Q123 102 247 118V142H0Z" fill="url(#cardFront3)"/>
  </svg>
  <div class="abs" style="left:30px;top:70px"><div class="wordmark" style="font-size:7.6px"><span class="dot" style="width:5px;height:5px"></span>Corvane Logistics</div></div>
  <div class="abs person" style="left:127px;top:18px"><div class="name">NADZRUL HAZIQ</div><div class="role">Managing Director</div></div>
  <ul class="abs contacts" style="left:127px;top:41px;font-size:5.2px;line-height:9px">
    <li><span class="ico" style="width:5px;height:5px"></span>+ 6012-480 2175</li>
    <li style="margin-top:4px"><span class="ico" style="width:5px;height:5px"></span>+ (603) 5520 1840 / 1850</li>
    <li><span class="ico" style="width:5px;height:5px"></span>+ (603) 5520 1860</li>
    <li style="margin-top:6px"><span class="ico" style="width:5px;height:5px"></span>nadzrul.haziq@corvane.com.my</li>
    <li class="web"><span class="ico" style="width:5px;height:5px;border-radius:50%"></span>www.<b>corvane</b>.com.my</li>
  </ul>
  <div class="abs center company" style="top:116px;font-size:5.6px">CORVANE LOGISTICS SDN. BHD. (1048326-K)</div>
  <div class="abs center address" style="top:127px;font-size:3.4px">No. 8B, 2nd Floor, Jalan Seroja Indah 3, Taman Perdana Kota, 41050 Klang, Selangor Darul Ehsan, Malaysia.</div>
</section>

<!-- Envelope front -->
<section class="sheet env-front" aria-label="Envelope front">
  <svg class="art" viewBox="0 0 456 232" preserveAspectRatio="none" aria-hidden="true">
    <defs><linearGradient id="envBlue" x1="0" y1="0" x2="1" y2="0"><stop offset="0" stop-color="#2f5ca8"/><stop offset="1" stop-color="#4c9dcc"/></linearGradient></defs>
    <path d="M0 0H456V18Q228 40 0 18Z" fill="#333"/>
    <path d="M0 202Q228 178 456 202V232H0Z" fill="url(#envBlue)"/>
  </svg>
  <div class="abs center slogan" style="top:9px;font-size:8.6px">ONE STOP LOGISTICS SOLUTIONS</div>
  <div class="abs" style="left:14px;top:70px"><div class="wordmark" style="font-size:8.6px"><span class="dot" style="width:5px;height:5px"></span>Corvane Logistics</div></div>
  <ul class="abs contacts" style="left:354px;top:45px;font-size:6px;line-height:10px">
    <li><span class="ico" style="width:6px;height:6px"></span>+ (603) 5520 1840 / 1850</li>
    <li><span class="ico" style="width:6px;height:6px"></span>+ (603) 5520 1860</li>
    <li class="web"><span class="ico" style="width:6px;height:6px;border-radius:50%"></span>www.<b>corvane</b>.com.my</li>
  </ul>
  <div class="abs center company" style="top:201px;font-size:8.4px">CORVANE LOGISTICS SDN. BHD. (1048326-K)</div>
  <div class="abs center address" style="top:216px;font-size:5.2px">No. 8B, 2nd Floor, Jalan Seroja Indah 3, Taman Perdana Kota, 41050 Klang, Selangor Darul Ehsan, Malaysia.</div>
</section>

<!-- Envelope back -->
<section class="sheet env-back" aria-label="Envelope back">
  <svg class="art" viewBox="0 0 456 232" preserveAspectRatio="none" aria-hidden="true">
    <defs><linearGradient id="flapBlue" x1="0" y1="0" x2="1" y2="0"><stop offset="0" stop-color="#2f5ca8"/><stop offset="1" stop-color="#4c9dcc"/></linearGradient></defs>
    <path d="M0 61Q228 76 456 60V64Q228 80 0 65Z" fill="#cfcfcf"/>
    <path d="M0 0H456V58Q228 74 0 59Z" fill="url(#flapBlue)"/>
  </svg>
</section>

</body>
</html>
```